Halvet Energy Letter Head- with all subsidiaries

We need a letterhead that will showcase all Halvet Energy subsidiaries, while still have Halvet Energy logo ontop.

```html
<!DOCTYPE html>
<html lang="en">
<head>
<meta charset="utf-8">
<title>Halvet Energy Letterhead</title>
<link href="https://fonts.googleapis.com/css2?family=Lato:wght@400;700&family=Yellowtail&display=swap" rel="stylesheet">
<style>
  :root {
    --backdrop: #e4e5e7;
    --paper: #ffffff;
    --gold: #c9a95d;
    --charcoal: #3d3e40;
    --body-text: #505153;
    --ink: #1e1e1e;
    --rule: #cfcfcf;
  }
  * { margin: 0; padding: 0; box-sizing: border-box; }
  html, body {
    width: 892px; height: 1200px; overflow: hidden;
    background: var(--backdrop);
    font-family: "Lato", Arial, sans-serif;
  }
  .letterhead {
    position: absolute; left: 51px; top: 41px;
    width: 790px; height: 1116px;
    background: var(--paper);
    overflow: hidden;
  }
  .brand {
    position: absolute; left: 54px; top: 58px;
    display: flex; align-items: center; gap: 12px;
  }
  .brand-square { width: 34px; height: 34px; background: var(--charcoal); }
  .brand-name {
    font-size: 40px; font-weight: 700; color: var(--charcoal);
    letter-spacing: 1px;
  }
  .contact {
    position: absolute; left: 579px; top: 53px;
    border-left: 1px solid var(--rule);
    padding-left: 10px;
    list-style: none;
    font-size: 12px; color: var(--ink);
  }
  .contact li { display: flex; align-items: center; gap: 5px; height: 19px; }
  .contact svg { width: 12px; height: 12px; }
  .letter {
    position: absolute; left: 58px; top: 284px; width: 674px;
    color: var(--body-text);
  }
  .salutation { font-size: 15px; font-weight: 700; color: var(--gold); margin-bottom: 21px; }
  .letter p.body {
    font-size: 15.2px; line-height: 24px; text-align: justify;
    margin-bottom: 17px;
  }
  .closing { font-size: 18px; color: var(--ink); margin-top: 26px; }
  .signature {
    font-family: "Yellowtail", cursive; font-size: 31px; color: var(--gold);
    margin-top: 4px;
  }
  .subsidiaries {
    position: absolute; left: 56px; top: 977px;
    display: grid; grid-template-columns: repeat(3, 92px);
    column-gap: 15px; row-gap: 18px;
  }
  .subsidiary {
    display: flex; align-items: center; gap: 4px; height: 38px;
    font-size: 10.5px; font-weight: 700; color: var(--charcoal); line-height: 1.1;
  }
  .subsidiary-mark { width: 10px; height: 10px; background: var(--gold); flex: none; }
  .footer-band { position: absolute; left: 0; bottom: 0; width: 790px; height: 130px; }
  .address {
    position: absolute; right: 56px; bottom: 18px;
    display: flex; align-items: center; gap: 5px;
    font-size: 12.5px; color: #ffffff;
  }
</style>
</head>
<body>
  <main class="letterhead">
    <header>
      <div class="brand">
        <span class="brand-square"></span>
        <span class="brand-name">Halvet Energy</span>
      </div>
      <ul class="contact">
        <li><svg viewBox="0 0 12 12"><circle cx="6" cy="6" r="5.3" fill="none" stroke="#c9a95d"/><rect x="4.3" y="3" width="3.4" height="6" rx=".6" fill="none" stroke="#c9a95d" stroke-width=".8"/></svg>012-555-0148</li>
        <li><svg viewBox="0 0 12 12"><circle cx="6" cy="6" r="5.3" fill="none" stroke="#c9a95d"/><rect x="3.2" y="4" width="5.6" height="4" fill="none" stroke="#c9a95d" stroke-width=".8"/><path d="M3.2 4 6 6.3 8.8 4" fill="none" stroke="#c9a95d" stroke-width=".8"/></svg>assist@halvetenergy.com</li>
        <li><svg viewBox="0 0 12 12"><circle cx="6" cy="6" r="5.3" fill="none" stroke="#c9a95d"/><ellipse cx="6" cy="6" rx="2.3" ry="5.3" fill="none" stroke="#c9a95d" stroke-width=".8"/><path d="M.7 6h10.6" stroke="#c9a95d" stroke-width=".8"/></svg>www.halvetenergy.com</li>
      </ul>
    </header>

    <section class="letter">
      <p class="salutation">Dear Mr. Lorem,</p>
      <p class="body">Lorem ipsum dolor sit amet, consectetuer adipiscing elit, sed diam nonummy nibh euismod tincidunt ut laoreet dolore magna aliquam erat volutpat. Ut wisi enim ad minim veniam, quis nostrud exerci tation ullamcorper suscipit lobortis nisl ut aliquip ex ea commodo consequat. Duis autem vel eum iriure dolor in hendiusto odio dignissim qui blandit praesent luptatum zzril delenit augue duis dolore te feugait nulla facilisi.</p>
      <p class="body">Lorem ipsum dolor sit amet, consectetuer adipiscing elit, sed diam nonummy nibh euismod tincidunt ut laoreet dolore magna aliquam erat volutpat. Ut wisi enim ad minim veniam, quis nostrud exerci tation ullamcorper suscipit lobortis nisl ut aliquip ex ea commodo consequat. Duis autem vel eum iriure dolor in hendiusto odio dignissim qui blandit praesent luptatum zzril delenit augue duis dolore te feugait nulla facilisi.</p>
      <p class="body">Lorem ipsum dolor sit amet, consectetuer adipiscing elit, sed diam nonummy nibh euismod tincidunt ut laoreet dolore magna aliquam erat volutpat. Ut wisi enim ad minim veniam, quis nostrud exerci tation ullamcorper suscipit lobortis nisl ut aliquip ex ea commodo consequat. Duis autem vel eum iriure dolor in hendiusto odio dignissim qui blandit praesent luptatum zzril delenit augue duis dolore te feugait nulla facilisi.</p>
      <p class="closing">Sincerely Your,</p>
      <p class="signature">Your Name</p>
    </section>

    <section class="subsidiaries" aria-label="Subsidiaries">
      <div class="subsidiary"><span class="subsidiary-mark"></span>Vantor Electric</div>
      <div class="subsidiary"><span class="subsidiary-mark"></span>Halvet Aviation</div>
      <div class="subsidiary"><span class="subsidiary-mark"></span>Halvet Acquisitions</div>
      <div class="subsidiary"><span class="subsidiary-mark"></span>Halvet Logistics</div>
      <div class="subsidiary"><span class="subsidiary-mark"></span>Halvet Caribbean</div>
      <div class="subsidiary"><span class="subsidiary-mark"></span>Upward Volt Electrical</div>
    </section>

    <footer>
      <svg class="footer-band" viewBox="0 0 790 130" preserveAspectRatio="none">
        <path d="M0 88 C 230 120 470 85 790 10 L790 130 L0 130 Z" fill="#3d3e40"/>
        <path d="M0 80 C 120 100 260 102 400 88 C 460 82 520 74 560 66 L560 68 C 500 82 300 108 0 88 Z" fill="#c9a95d"/>
      </svg>
      <div class="address">
        <svg width="12" height="12" viewBox="0 0 12 12"><circle cx="6" cy="6" r="5.3" fill="none" stroke="#fff"/><path d="M6 9.3 C4.2 7.3 3.8 6.3 3.8 5.2 a2.2 2.2 0 0 1 4.4 0 c0 1.1-.4 2.1-2.2 4.1z" fill="none" stroke="#fff" stroke-width=".8"/><circle cx="6" cy="5.2" r=".7" fill="#fff"/></svg>
        Street Name, City Name, Zipcode-01234
      </div>
    </footer>
  </main>
</body>
</html>
```